Kestrel Flooring Supply

Basic one-sided business card design using the attached logo. Vintage americana theme. Font is modified Arial Nova Cond, but anything that coordinates can be used

```html
<!DOCTYPE html>
<html lang="en">
<head>
<meta charset="utf-8">
<title>Kestrel Flooring Supply – Business Card</title>
<link href="https://fonts.googleapis.com/css2?family=Poppins:wght@400;600&family=Roboto:wght@700&display=swap" rel="stylesheet">
<style>
  :root {
    --backdrop: #e9e6e2;
    --card: #030303;
    --gold: #b49a78;
    --white: #ffffff;
  }
  * { box-sizing: border-box; margin: 0; padding: 0; }
  html, body {
    width: 1200px; height: 900px; overflow: hidden;
    background: var(--backdrop);
  }
  .business-card {
    position: absolute; left: 150px; top: 172px;
    width: 900px; height: 556px;
    background: var(--card);
    border-radius: 0 280px 280px 0 / 0 278px 278px 0;
    font-family: "Poppins", sans-serif;
    color: var(--white);
  }
  .person { position: absolute; left: 37px; top: 72px; }
  .person-name {
    font-family: "Roboto", sans-serif; font-weight: 700;
    font-size: 40px; line-height: 1; color: var(--gold);
  }
  .person-title { font-size: 27px; line-height: 1.3; margin-top: 2px; }
  .contact-list {
    position: absolute; left: 37px; top: 258px; list-style: none;
  }
  .contact-item {
    display: flex; align-items: center; gap: 10px;
    font-size: 27px; line-height: 33px;
  }
  .contact-icon { width: 24px; height: 24px; flex: none; }
  .address {
    position: absolute; left: 37px; top: 432px;
    font-size: 27px; line-height: 33px; font-style: normal;
  }
  .brand {
    position: absolute; left: 600px; top: 238px;
    width: 300px;
    display: flex; align-items: center; gap: 14px;
  }
  .brand-dot {
    width: 18px; height: 18px; flex: none;
    border-radius: 50%; background: var(--gold);
  }
  .brand-name {
    font-size: 30px; font-weight: 600; line-height: 1.25;
    color: var(--white);
  }
</style>
</head>
<body>
  <section class="business-card">
    <div class="person">
      <h1 class="person-name">DANIEL HARTLEY</h1>
      <p class="person-title">Managing Director</p>
    </div>

    <ul class="contact-list">
      <li class="contact-item">
        <svg class="contact-icon" viewBox="0 0 24 24" fill="none" stroke="var(--gold)" stroke-width="2" stroke-linecap="round">
          <path d="M5 3h4l2 5-2.5 1.5a11 11 0 0 0 6 6L16 13l5 2v4a2 2 0 0 1-2 2A16 16 0 0 1 3 5a2 2 0 0 1 2-2z"/>
          <path d="M15 3a6 6 0 0 1 6 6M15 7a2 2 0 0 1 2 2"/>
        </svg>
        044-310 582 467
      </li>
      <li class="contact-item">
        <svg class="contact-icon" viewBox="0 0 24 24" fill="var(--gold)">
          <path d="M1 5h22v14H1z"/>
          <path d="M1 5l11 8 11-8" fill="none" stroke="var(--card)" stroke-width="1.6"/>
        </svg>
        info@kestrelfloors.com
      </li>
      <li class="contact-item">
        <svg class="contact-icon" viewBox="0 0 24 24" fill="none" stroke="var(--gold)" stroke-width="1.8">
          <circle cx="12" cy="12" r="10"/>
          <ellipse cx="12" cy="12" rx="4.5" ry="10"/>
          <path d="M2 12h20M4 7h16M4 17h16"/>
        </svg>
        www.kestrelfloors.com
      </li>
    </ul>

    <address class="address">
      421, Address line goes here<br>
      45452,Country Name
    </address>

    <div class="brand">
      <span class="brand-dot"></span>
      <span class="brand-name">Kestrel Flooring Supply</span>
    </div>
  </section>
</body>
</html>
```